Companybrochure for Consulting & Financing Firm

I need to have a Company Brochure asap for our company. We have a website that describes what we do, but we need also a brochure, that can be sent by PDF of eventually be printed as well.

The brochure should be short but nice and appealing to the customers.

We provide professional management consulting and help our customers to get finance for very diferent projects. Our business has a lot to do with personal relations, but also we are very professional in the way we work and how develop the solutions for our clients. Our clients are mainly government-owned firm, but also private trading companies and wealthy private investors.

Our customers are mainly in Latin America, but the company is headquater is in Switzerland. We are opening offices in Panama and Caracas, this should be easaly be adabtable later.

Please have a look at our website www.brevalto.ch. In the brochure, we would segment our services in 1.) Project Developments 2.) Management Conulting 3.) Investment Management and 4.) Finance Solutions.

Also do have a look at www.brevalto.ch
(Click E for the English version)

I managed to put the Mock-Up to the Website.
It is actually not really a mock-up, it is a version I have designed myself.
Well as I am not a designer, I hope you can make it much better.
The content however is what I would put in any other design as well.

Target Market(s)

Top Management, Investors, Entrepreneurs, Government Officials

Industry/Entity Type

Management Consulting

Requirements
Must have
• Design should reflect this image elements:

We are entrepreneurs.
We are comitted to get things done.
We work closely with the client side by side.
We are a professional partner.
We are not afraid of delivering unconventional solutions.
We look at the problem from various angles.
We analyse, develop solutions and implent results.
Should not have
• Typical US-American style elements. We do not want to give the impression of being a US company.

We do not want to appear to be neo-liberal. We are a politically neutral professional consulting firm.

```html
<!DOCTYPE html>
<html lang="en">
<head>
<meta charset="utf-8">
<title>Brevalto AG – Brochure</title>
<link href="https://fonts.googleapis.com/css2?family=Oswald:wght@500;600;700&family=Source+Sans+3:wght@400;600;700&display=swap" rel="stylesheet">
<style>
  :root {
    --bg: #e9e7e4;
    --paper: #ffffff;
    --charcoal: #333335;
    --charcoal-soft: rgba(40, 40, 42, 0.82);
    --navy: #2a2563;
    --bar-grey: #d6d6d6;
    --ink: #3a3a3c;
    --white: #ffffff;
    --night: #0b1220;
    --dusk: #1d2a3a;
    --lawn: #3f8f2a;
    --condensed: "Oswald", "Arial Narrow", sans-serif;
    --text: "Source Sans 3", "Myriad Pro", sans-serif;
  }
  * { margin: 0; padding: 0; box-sizing: border-box; }
  html, body { width: 1200px; height: 960px; overflow: hidden; }
  body { background: var(--bg); position: relative; font-family: var(--text); }

  .page {
    position: absolute; top: 103px; width: 541px; height: 764px;
    background: var(--paper); overflow: hidden;
    box-shadow: 0 4px 14px rgba(0,0,0,0.18);
  }
  .page--back { left: 45px; }
  .page--front { left: 615px; }
  .shapes { position: absolute; inset: 0; }

  /* back page */
  .values { position: absolute; left: 206px; top: 280px; width: 330px; color: var(--white); }
  .values__title {
    font-family: var(--condensed); font-weight: 600; font-size: 27px;
    letter-spacing: 0.2px; line-height: 1; margin-bottom: 16px; white-space: nowrap;
  }
  .values__list { list-style: none; font-weight: 600; font-size: 14px; line-height: 1.05; }
  .values__list li { margin-bottom: 11px; padding-left: 13px; text-indent: -13px; }

  .brand-line {
    position: absolute; left: 194px; top: 566px;
    font-family: var(--text); font-weight: 700; font-size: 24px; color: var(--ink);
  }

  .contact {
    position: absolute; left: 24px; top: 402px; color: var(--white);
    font-size: 11.5px; line-height: 1.25;
  }
  .contact p + p { margin-top: 11px; }

  .registered {
    position: absolute; left: 68px; top: 563px; width: 107px;
    color: var(--white); text-align: center;
    font-family: var(--condensed); font-weight: 500; font-size: 12.5px; line-height: 1.25;
  }

  /* front page */
  .cover-visual { position: absolute; left: 27px; top: 0; width: 486px; height: 731px; }
  .cover-name {
    position: absolute; left: 126px; top: 26px; width: 387px; height: 52px;
    background: var(--bar-grey); color: var(--ink);
    font-family: var(--text); font-weight: 700; font-size: 38px; line-height: 52px;
    padding-left: 8px; white-space: nowrap;
  }
  .services { position: absolute; left: 194px; top: 493px; width: 205px; color: var(--white); }
  .services__intro {
    font-family: var(--condensed); font-weight: 600; font-size: 17px; line-height: 1.07;
    margin-bottom: 12px;
  }
  .services__list { list-style: none; font-size: 15px; line-height: 1.35; }
  .motto {
    position: absolute; left: 55px; top: 598px; width: 113px;
    color: var(--white); text-align: center;
    font-family: var(--condensed); font-weight: 600; font-size: 26px; line-height: 1.12;
  }
</style>
</head>
<body>

<section class="page page--back">
  <svg class="shapes" width="541" height="764" viewBox="0 0 541 764">
    <polygon fill="var(--charcoal)" points="280,195 541,195 541,486 469,559 191,559 191,281"/>
    <polygon fill="var(--navy)" points="44,362 175,362 175,508 139,544 0,544 0,404"/>
    <polygon fill="var(--navy)" points="68,555 175,555 175,649 156,668 68,668"/>
  </svg>

  <div class="values">
    <h2 class="values__title">ANALYZE • DEVELOP • DELIVER</h2>
    <ul class="values__list">
      <li>&gt; We are entrepreneurs.</li>
      <li>&gt; We are comitted to get things done.</li>
      <li>&gt; We work closely with the client side by side.</li>
      <li>&gt; We are a professional partner.</li>
      <li>&gt; We are not afraid of delivering unconventional solutions.</li>
      <li>&gt; We look at the problem from various angles</li>
      <li>&gt; We analyse, develop solutions and implent results.</li>
    </ul>
  </div>

  <div class="brand-line">Brevalto AG</div>

  <address class="contact">
    <p>Brevalto AG<br>Lindenhofweg 7<br>CH-8048 Zürich</p>
    <p>Tel.&nbsp; +41 44 555 01 20<br>Fax. +41 44 555 01 29</p>
    <p>www.brevalto.ch<br>info@brevalto.ch</p>
  </address>

  <p class="registered">Brevalto AG is registered as a Swiss stock corporation since 1995.</p>
</section>

<section class="page page--front">
  <svg class="cover-visual" width="486" height="731" viewBox="0 0 486 731" role="img" aria-label="Night photograph of construction cranes and a lit street lamp above a green lawn beside a new building">
    <defs>
      <linearGradient id="night-site" x1="0" y1="0" x2="0" y2="1">
        <stop offset="0" stop-color="var(--night)"/>
        <stop offset="0.45" stop-color="var(--dusk)"/>
        <stop offset="0.72" stop-color="#2f4a3a"/>
        <stop offset="1" stop-color="var(--lawn)"/>
      </linearGradient>
    </defs>
    <polygon fill="url(#night-site)" points="0,0 486,0 486,673 427,731 0,731"/>
  </svg>

  <div class="cover-name">Brevalto AG</div>

  <svg class="shapes" width="541" height="764" viewBox="0 0 541 764">
    <polygon fill="var(--charcoal-soft)" points="210,469 405,469 405,708 175,708 175,504"/>
    <polygon fill="var(--navy)" points="55,593 150,593 168,611 168,709 55,709"/>
  </svg>

  <div class="services">
    <p class="services__intro">We are a professional consulting, financing and investment firm operating in the fields of:</p>
    <ul class="services__list">
      <li>&gt; Project Development</li>
      <li>&gt; Management Consulting</li>
      <li>&gt; Investment Management</li>
      <li>&gt; Finance Solutions</li>
    </ul>
  </div>

  <p class="motto">ANALYZE<br>DEVELOP<br>DELIVER</p>
</section>

</body>
</html>
```